Real Estate Agent Announcement

I need an announcement postcard designed with imagery almost exactly similar to below; one side imagery and copy on the other. Palette is either desired in neutrals: off white, warm white, or very soft grey. I'd like to stick as close to example below in feeling of image evoking opulence and text to be clean and elegant. need double sided card with simple logo on the back. copy of logo attached. editable file type.

Target Market(s)

Luxury real estate market northern california

Industry/Entity Type

Real Estate

Font styles to use
Serif

```html
<!DOCTYPE html>
<html lang="en">
<head>
<meta charset="utf-8">
<title>Naomi Castell — Announcement</title>
<link rel="stylesheet" href="https://fonts.googleapis.com/css2?family=Gafata&display=swap">
<style>
  :root {
    --page: #ffffff;
    --panel-light: #fbfbfb;
    --panel-edge: #e9e9e9;
    --ink: #6d6d6d;
    --ink-soft: #7a7a7a;
    --rule: #8a8a8a;
    --photo-cream: #efe7d6;
    --photo-beige: #cdb795;
    --photo-rose: #b58a73;
    --photo-wood: #6e5541;
  }
  * { margin: 0; padding: 0; box-sizing: border-box; }
  html, body {
    width: 1200px;
    height: 863px;
    overflow: hidden;
    background: var(--page);
  }
  .postcard {
    position: relative;
    width: 1200px;
    height: 863px;
    background: var(--page);
    font-family: "Gafata", sans-serif;
    color: var(--ink);
  }
  .interior-photo {
    position: absolute;
    left: 22px;
    top: 22px;
    width: 578px;
    height: 819px;
    background:
      radial-gradient(ellipse at 85% 30%, rgba(239,231,214,0.9), transparent 45%),
      radial-gradient(ellipse at 70% 85%, rgba(181,138,115,0.8), transparent 50%),
      radial-gradient(ellipse at 45% 55%, rgba(110,85,65,0.55), transparent 45%),
      linear-gradient(160deg, var(--photo-cream) 0%, var(--photo-beige) 55%, var(--photo-rose) 100%);
  }
  .message-panel {
    position: absolute;
    left: 600px;
    top: 22px;
    width: 578px;
    height: 819px;
    background: radial-gradient(ellipse at 50% 35%, var(--panel-light) 0%, #f4f4f4 60%, var(--panel-edge) 100%);
    text-align: center;
  }
  .agent-name {
    position: absolute;
    top: 195px;
    width: 100%;
    font-size: 47px;
    font-weight: 400;
    letter-spacing: 1px;
    color: var(--ink);
  }
  .announcement {
    position: absolute;
    top: 288px;
    width: 100%;
    font-size: 24px;
    line-height: 34px;
    color: var(--ink-soft);
  }
  .values {
    position: absolute;
    top: 460px;
    width: 100%;
    font-size: 24px;
    line-height: 35px;
    color: var(--ink-soft);
  }
  .values .pillars { letter-spacing: 0.5px; }
  .network-mark {
    position: absolute;
    top: 650px;
    width: 100%;
    display: flex;
    justify-content: center;
    align-items: center;
    gap: 10px;
    font-size: 21px;
    color: var(--ink);
  }
  .network-mark .dot {
    width: 12px;
    height: 12px;
    border-radius: 50%;
    background: var(--ink);
  }
  .office-address {
    position: absolute;
    top: 744px;
    width: 100%;
    font-size: 17px;
    line-height: 23px;
    color: var(--ink-soft);
  }
</style>
</head>
<body>
  <main class="postcard">
    <div class="interior-photo" role="img" aria-label="Photograph of an opulent bedroom with a canopy bed, floral valance, tufted armchair and ottoman, fireplace with round mirror and lantern chandelier"></div>

    <section class="message-panel">
      <h1 class="agent-name">NAOMI CASTELL</h1>
      <p class="announcement">is pleased to announce<br>her affiliation with<br>Harbor Crest Realty.</p>
      <p class="values"><span class="pillars">INTEGRITY | KNOWLEDGE</span><br>all of your needs.</p>
      <div class="network-mark">
        <span class="dot"></span>
        <span class="network-name">The Lena Morrow Network</span>
      </div>
      <address class="office-address" style="font-style: normal;">418 Oak Meadow Dr. Ste. 100<br>Alder Creek, CA 94599</address>
    </section>
  </main>
</body>
</html>
```